Bright Harbor Web Design & Marketing

Will award a 2nd place prize of $100.00 if someone can come up with a logo to match this design!
Updates

Okay, I'm really looking to see some better designs here. What do you think will bring the best designs out? Please remember with all future submissions I'm looking for a cartoon style / illustrator style website. I'm not sure what the technical term is for it, so I uploaded some images in the brief.

Target Market(s)

Small Business Owners

Industry/Entity Type

Marketing

Logo Text

BrightHarborly.com

Number of Pages Required

1 page

Colors

Designer to choose colors to be used in the design.

Requirements
Must have
• Logo should say BrightHarborly.com I would like more than just a text logo. I want some sort of cool custom graphic / icon with it that will look nice on shirts/hats/etc

```html
<!DOCTYPE html>
<html lang="en">
<head>
<meta charset="utf-8">
<title>Bright Harbor Web Design &amp; Marketing</title>
<link rel="stylesheet" href="https://fonts.googleapis.com/css2?family=Montserrat:wght@400;500;600;700;800&family=Raleway:wght@500;600;700;800&display=swap">
<style>
:root{
  --teal:#2ab6b2;
  --teal-mid:#1fa9a5;
  --teal-deep:#178f8c;
  --teal-pale:#a8dcd9;
  --dark:#1d5452;
  --ink:#1f2b2c;
  --grey:#6b7677;
  --paper:#ffffff;
  --mist:#f0f0f0;
  --grass:#6cbf45;
}
*{margin:0;padding:0;box-sizing:border-box}
html,body{width:1200px;height:3636px;overflow:hidden}
body{position:relative;background:var(--paper);font-family:"Montserrat",sans-serif;color:var(--ink)}
.abs{position:absolute}
.center{text-align:center}

/* hero */
.hero{top:0;left:0;width:1200px;height:674px;background:var(--teal)}
.topbar{top:8px;left:218px;font-size:9px;color:#e6fbfa;letter-spacing:.5px;display:flex;gap:36px;align-items:center}
.topbar span{display:flex;align-items:center;gap:6px}
.brand{top:34px;left:218px;display:flex;align-items:center;gap:8px;color:var(--paper);font-weight:700;font-size:11px}
.brand-dot{width:34px;height:34px;border-radius:50%;background:var(--paper)}
.nav{top:53px;left:415px;display:flex;font-family:"Raleway",sans-serif;font-weight:700;font-size:9.5px;letter-spacing:1.8px;color:var(--paper)}
.nav a{color:inherit;text-decoration:none;width:134px;text-align:center;padding-bottom:6px}
.nav a.active{border-bottom:2px solid var(--paper);width:60px;margin:0 37px}
.cta-top{top:6px;left:866px;width:116px;height:22px;background:#3fd5e0;color:var(--paper);font-size:8px;font-weight:700;letter-spacing:1px;display:flex;align-items:center;justify-content:center}
.hero-kicker{top:126px;left:0;width:1200px;font-family:"Raleway",sans-serif;font-weight:800;font-size:14px;letter-spacing:5px;color:#e8fbfa}
.hero-title{top:150px;left:0;width:1200px;font-family:"Raleway",sans-serif;font-weight:800;font-size:58px;line-height:66px;letter-spacing:10px;color:var(--paper)}
.btn{top:321px;height:28px;width:124px;display:flex;align-items:center;justify-content:center;font-size:8.5px;font-weight:700;letter-spacing:1.6px}
.btn-solid{left:465px;background:#38dbe6;color:var(--paper)}
.btn-light{left:611px;background:var(--paper);color:var(--ink)}
.skyline{top:360px;left:0;width:1200px;height:300px;background:linear-gradient(180deg,rgba(42,182,178,0) 0%,#4fb3b4 30%,#6c9fa8 60%,#8a8f98 85%,#7f8c92 100%)}
.grass{top:650px;left:0;width:1200px;height:24px;background:linear-gradient(180deg,var(--grass) 0%,#52a83a 100%)}

/* differences */
.section-title{font-weight:700;font-size:17px;letter-spacing:.6px;color:var(--ink)}
.diff-title{top:745px;left:0;width:1200px}
.diff-item{top:812px;width:220px}
.diff-art{width:110px;height:98px;margin:0 auto;border-radius:50%;background:radial-gradient(circle at 50% 45%,#fbe6d6 0%,#e3f3f2 55%,#f4fbfb 85%,#ffffff 100%)}
.diff-label{margin-top:24px;font-weight:700;font-size:11.5px;line-height:15px;color:var(--teal);letter-spacing:.4px}

/* how we work */
.work{top:1023px;left:0;width:1200px;height:499px;background:radial-gradient(ellipse at 50% 40%,#d4efe9 0%,var(--teal-pale) 45%,#9fd3d1 100%)}
.play{border-radius:50%;background:var(--teal-mid);border:5px solid rgba(255,255,255,.55);display:flex;align-items:center;justify-content:center}
.work-play{top:1204px;left:560px;width:78px;height:78px}
.work-label{top:1338px;left:0;width:1200px;font-weight:700;font-size:16px;color:var(--paper);letter-spacing:.5px}

/* services */
.services{top:1522px;left:0;width:1200px;height:737px;background:linear-gradient(160deg,#38bdb8 0%,var(--teal) 50%,#26aaa6 100%)}
.kicker-small{top:1582px;left:0;width:1200px;font-size:8px;font-weight:700;letter-spacing:1px;color:var(--paper)}
.services-title{top:1598px;left:0;width:1200px;font-weight:700;font-size:19px;color:var(--paper)}
.service{width:220px;text-align:center}
.service-icon{width:116px;height:116px;margin:0 auto;border-radius:50%;background:var(--paper);border:3px solid var(--teal-deep);display:flex;align-items:center;justify-content:center}
.service-label{margin-top:14px;font-size:10.5px;font-weight:600;line-height:14px;color:var(--paper);letter-spacing:.3px}

/* team */
.team-title{top:2322px;left:0;width:1200px}
.card{top:2393px;width:233px;height:327px;background:#dfe8e8;overflow:hidden}
.card-photo{position:absolute;inset:0;background:linear-gradient(160deg,#eef1ef 0%,#d8c2b0 45%,#b9a596 100%)}
.card-band{position:absolute;left:0;bottom:0;width:100%;height:83px;background:var(--teal);color:var(--paper);text-align:center;padding-top:28px}
.card-name{font-family:"Raleway",sans-serif;font-size:9px;font-weight:700;letter-spacing:2.5px}
.card-role{margin-top:5px;font-size:6.5px;letter-spacing:.8px;opacity:.9}
.card-full .card-photo{background:linear-gradient(180deg,#36b8b3 0%,#2aa9a5 100%)}
.card-full .card-text{position:absolute;top:60px;left:26px;right:26px;color:var(--paper);text-align:center}
.card-full .card-band{background:#23a29e}

/* feedback */
.video-side{top:2819px;left:0;width:592px;height:412px;background:linear-gradient(160deg,#5ac7c2 0%,#3bb7b2 50%,#2ea9a5 100%)}
.video-play{top:2980px;left:243px;width:96px;height:96px}
.feedback{top:2819px;left:592px;width:608px;height:412px;background:var(--mist)}
.feedback-title{top:2883px;left:592px;width:608px;font-size:16px}
.avatar{top:2934px;left:842px;width:120px;height:120px;border-radius:50%;border:4px solid var(--teal);background:radial-gradient(circle,#e9d6c5 0%,#c7b2a0 60%,#9fb8b6 100%)}
.quote{top:3070px;left:690px;width:420px;font-size:11.5px;line-height:17px;color:#4a5556}
.quote-by{top:3145px;left:592px;width:608px;font-size:10px;color:var(--grey)}
.dots{top:3187px;left:872px;display:flex;gap:14px}
.dots i{width:6px;height:6px;border-radius:50%;background:#c4c4c4;display:block}
.dots i.on{background:var(--teal)}

/* footer */
.footer{top:3231px;left:0;width:1200px;height:344px;background:var(--teal)}
.foot-brand{top:3287px;left:235px;display:flex;align-items:center;gap:8px;color:var(--paper);font-weight:700;font-size:10px}
.foot-brand .brand-dot{width:28px;height:28px}
.foot-text{left:235px;width:320px;font-size:9.5px;line-height:15px;color:#eafcfb}
.foot-head{font-family:"Raleway",sans-serif;font-size:9px;font-weight:700;letter-spacing:4px;color:var(--paper)}
.news{left:606px;width:180px;display:flex;gap:14px}
.news-thumb{width:34px;height:34px;background:#e8eded;flex:none}
.news-title{font-size:8.5px;font-weight:700;color:var(--paper);line-height:12px}
.news-date{font-size:7.5px;color:#d4f4f2;margin-top:3px}
.news-rule{left:606px;width:175px;height:1px;background:rgba(255,255,255,.35)}
.subscribe-text{left:795px;width:190px;font-size:8.5px;line-height:13px;color:#eafcfb}
.sub-field{top:3410px;left:795px;width:175px;height:30px;border:1px solid rgba(255,255,255,.7);display:flex}
.sub-field span{flex:1;font-size:8px;color:#d4f4f2;padding:10px 8px}
.sub-field b{width:30px;border-left:1px solid rgba(255,255,255,.7);display:flex;align-items:center;justify-content:center}
.sub-note{top:3448px;left:795px;font-size:7.5px;color:#d4f4f2}
.bottom-bar{top:3575px;left:0;width:1200px;height:61px;background:var(--dark)}
.copyright{top:3598px;left:235px;font-size:8.5px;color:#b6d6d4}
.social{top:3594px;display:block;width:22px;height:22px;border-radius:50%;background:var(--teal)}
</style>
</head>
<body>

<!-- hero -->
<section class="abs hero" aria-label="Hero"></section>
<div class="abs skyline" role="img" aria-label="Flat cartoon city skyline with a tall needle tower and office buildings"></div>
<div class="abs grass" role="img" aria-label="Green strip of trees along the base of the skyline"></div>
<div class="abs topbar">
  <span><svg width="11" height="8" viewBox="0 0 11 8"><rect x=".5" y=".5" width="10" height="7" fill="none" stroke="#fff"/><path d="M.5 .5 5.5 4.5 10.5 .5" fill="none" stroke="#fff"/></svg>HELLO@BRIGHTHARBORLY.COM</span>
  <span><svg width="9" height="9" viewBox="0 0 9 9"><path d="M1 1.5 3 1l1 2-1 1a5 5 0 0 0 2 2l1-1 2 1-.5 2C4 8 1 5 1 1.5Z" fill="#fff"/></svg>PHONE: +1 (555) 014-2290</span>
</div>
<div class="abs cta-top">CONTACT US NOW</div>
<div class="abs brand"><span class="brand-dot"></span>BrightHarborly.com</div>
<nav class="abs nav">
  <a class="active">HOME</a><a>SERVICES &amp; PRICING</a><a>OUR TEAM</a><a>CLIENTS/PORTFOLIO</a><a>CONTACT US</a>
</nav>
<p class="abs hero-kicker center">THE DESIGN &amp; MARKETING TEAM THAT ALWAYS PUTS</p>
<h1 class="abs hero-title center">TRUST &amp; LOYALTY<br>BEFORE PROFITS</h1>
<a class="abs btn btn-solid">CONTACT US</a>
<a class="abs btn btn-light">PORTFOLIO</a>

<!-- what makes us different -->
<h2 class="abs section-title diff-title center">WHAT MAKES US DIFFERENT?</h2>
<div class="abs diff-item center" style="left:241px">
  <div class="diff-art" role="img" aria-label="Cartoon illustration of a risk free investment certificate"></div>
  <p class="diff-label">100% RISK FREE<br>INVESTMENT</p>
</div>
<div class="abs diff-item center" style="left:489px">
  <div class="diff-art" role="img" aria-label="Cartoon illustration of a magnet attracting coins"></div>
  <p class="diff-label">CUSTOMER LOYALTY<br>PROGRAM</p>
</div>
<div class="abs diff-item center" style="left:743px">
  <div class="diff-art" role="img" aria-label="Cartoon illustration of a support agent with a headset"></div>
  <p class="diff-label">24/7 U.S. BASED<br>CUSTOMER SUPPORT</p>
</div>

<!-- how we work -->
<section class="abs work" role="img" aria-label="Faded illustration of a large light bulb over a laptop surrounded by office icons"></section>
<div class="abs play work-play"><svg width="20" height="22" viewBox="0 0 20 22"><path d="M3 2 18 11 3 20Z" fill="none" stroke="#fff" stroke-width="2"/></svg></div>
<p class="abs work-label center">HOW WE WORK</p>

<!-- services -->
<section class="abs services" role="img" aria-label="Teal tinted photo of a desk with keyboards, hands and design sketches"></section>
<p class="abs kicker-small center">OUR SERVICES</p>
<h2 class="abs services-title center">WHAT SERVICES DO WE OFFER?</h2>

<div class="abs service" style="left:241px;top:1644px">
  <div class="service-icon"><svg width="56" height="48" viewBox="0 0 56 48" fill="none" stroke="#178f8c" stroke-width="2.5"><rect x="3" y="3" width="50" height="32" rx="3"/><path d="M20 45h16M28 35v10M10 12h36M10 20h20M10 27h26"/></svg></div>
  <p class="service-label">WEBSITE DESIGN &amp;<br>MANAGEMENT</p>
</div>
<div class="abs service" style="left:489px;top:1644px">
  <div class="service-icon"><svg width="50" height="50" viewBox="0 0 50 50" fill="none" stroke="#178f8c" stroke-width="2.5"><rect x="4" y="10" width="42" height="30" rx="2"/><path d="M12 34 34 12l4 4-22 22h-4z M4 46h42"/></svg></div>
  <p class="service-label">LOGO DESIGN &amp;<br>BRANDING MATERIALS</p>
</div>
<div class="abs service" style="left:743px;top:1644px">
  <div class="service-icon"><svg width="56" height="46" viewBox="0 0 56 46" fill="none" stroke="#178f8c" stroke-width="2.5"><rect x="3" y="3" width="50" height="34" rx="3"/><path d="M3 12h50M18 24h6l3 8h12l3-8H28"/><circle cx="30" cy="41" r="2"/><circle cx="38" cy="41" r="2"/></svg></div>
  <p class="service-label">ONLINE STORE DESIGN &amp;<br>MANAGEMENT</p>
</div>

<div class="abs service" style="left:241px;top:1835px">
  <div class="service-icon"><svg width="50" height="50" viewBox="0 0 50 50" fill="none" stroke="#178f8c" stroke-width="2.5"><path d="M6 20 10 6h30l4 14Z"/><rect x="8" y="20" width="34" height="26"/><rect x="14" y="28" width="9" height="18"/><rect x="28" y="28" width="9" height="8"/></svg></div>
  <p class="service-label">LOCAL SEO<br>MANAGEMENT</p>
</div>
<div class="abs service" style="left:489px;top:1835px">
  <div class="service-icon"><svg width="50" height="50" viewBox="0 0 50 50" fill="none" stroke="#178f8c" stroke-width="2.5"><circle cx="21" cy="21" r="15"/><path d="M32 32 46 46M12 21h18M21 12v18"/></svg></div>
  <p class="service-label">SEARCH ENGINE<br>OPTIMIZATION</p>
</div>
<div class="abs service" style="left:743px;top:1835px">
  <div class="service-icon"><svg width="50" height="50" viewBox="0 0 50 50" fill="none" stroke="#178f8c" stroke-width="2.5"><rect x="4" y="22" width="9" height="22"/><path d="M13 24l9-14c3-4 7-2 6 3l-2 7h14c3 0 5 3 4 6l-4 14c-1 2-3 3-5 3H13"/></svg></div>
  <p class="service-label">SOCIAL MEDIA<br>MARKETING</p>
</div>

<div class="abs service" style="left:241px;top:2027px">
  <div class="service-icon"><svg width="46" height="52" viewBox="0 0 46 52" fill="none" stroke="#178f8c" stroke-width="2.5"><rect x="4" y="4" width="30" height="44" rx="2"/><path d="M11 16h16M11 24h16M11 32h10M40 10v30l-3 6-3-6V10z"/></svg></div>
  <p class="service-label">MARKETING MATERIAL<br>&amp; PRINT DESIGN</p>
</div>
<div class="abs service" style="left:489px;top:2027px">
  <div class="service-icon"><svg width="56" height="46" viewBox="0 0 56 46" fill="none" stroke="#178f8c" stroke-width="2.5"><rect x="4" y="8" width="48" height="32" rx="3"/><circle cx="28" cy="24" r="9"/><path d="M12 8V4h10v4"/></svg></div>
  <p class="service-label">OUTSOURCING<br>MANAGEMENT</p>
</div>
<div class="abs service" style="left:743px;top:2027px">
  <div class="service-icon"><svg width="44" height="52" viewBox="0 0 44 52" fill="none" stroke="#178f8c" stroke-width="2.5"><circle cx="22" cy="12" r="8"/><path d="M6 46V34c0-7 7-12 16-12s16 5 16 12v12M2 46h40M14 32h16v14H14z"/></svg></div>
  <p class="service-label">CONSULTING</p>
</div>

<!-- team -->
<h2 class="abs section-title team-title center">MEET OUR TEAM</h2>
<article class="abs card" style="left:109px">
  <div class="card-photo" role="img" aria-label="Portrait photo of a smiling team member in a white shirt"></div>
  <div class="card-band"><p class="card-name">EVAN HALE</p><p class="card-role">CHIEF EXECUTIVE OFFICER</p></div>
</article>
<article class="abs card card-full" style="left:361px">
  <div class="card-photo" role="img" aria-label="Teal tinted portrait photo of a team member"></div>
  <div class="card-text">
    <p class="card-name">MARCO REYES</p>
    <p class="card-role">LEAD CREATIVE DIRECTOR</p>
    <p style="margin-top:14px;font-size:7.5px;line-height:12px">Leads every brand project from first sketch to final launch, keeping each design simple, bold and true to the client.</p>
  </div>
  <div class="card-band"></div>
</article>
<article class="abs card" style="left:608px">
  <div class="card-photo" role="img" aria-label="Portrait photo of a laughing team member on the phone"></div>
  <div class="card-band"><p class="card-name">LENA BROOKS</p><p class="card-role">HEAD OF CLIENT SUPPORT</p></div>
</article>
<article class="abs card" style="left:861px">
  <div class="card-photo" role="img" aria-label="Portrait photo of a smiling team member in a striped top"></div>
  <div class="card-band"><p class="card-name">SOFIA LANE</p><p class="card-role">MARKETING STRATEGIST</p></div>
</article>

<!-- feedback -->
<section class="abs video-side" role="img" aria-label="Teal tinted photo of a client in glasses for a video testimonial"></section>
<div class="abs play video-play"><svg width="22" height="24" viewBox="0 0 22 24"><path d="M4 2 20 12 4 22Z" fill="none" stroke="#fff" stroke-width="2"/></svg></div>
<section class="abs feedback" aria-label="Clients feedback"></section>
<h2 class="abs section-title feedback-title center">CLIENTS FEEDBACK</h2>
<div class="abs avatar" role="img" aria-label="Round portrait photo of the client"></div>
<p class="abs quote center">"Donec eget tellus non erat lacinia fermentum. Donec in velit vel ipsum auctor pulvinar. Vestibulum iaculis lacinia est. Proin dictum elementum velit."</p>
<p class="abs quote-by center">Evan Hale</p>
<div class="abs dots"><i></i><i class="on"></i><i></i></div>

<!-- footer -->
<footer class="abs footer"></footer>
<div class="abs foot-brand"><span class="brand-dot"></span>BrightHarborly.com</div>
<p class="abs foot-text" style="top:3336px">We build clear, friendly websites and marketing plans that help small local businesses grow with confidence.</p>
<p class="abs foot-text" style="top:3388px">Every project comes with honest pricing, steady support and a team that answers the phone.</p>

<p class="abs foot-head" style="top:3298px;left:606px">LATEST NEWS</p>
<div class="abs news" style="top:3330px"><span class="news-thumb"></span><div><p class="news-title">Five simple ways to win repeat local customers</p><p class="news-date">Mar 12, 2017</p></div></div>
<div class="abs news-rule" style="top:3380px"></div>
<div class="abs news" style="top:3400px"><span class="news-thumb"></span><div><p class="news-title">Why a fast website keeps visitors around longer</p><p class="news-date">Mar 04, 2017</p></div></div>
<div class="abs news-rule" style="top:3450px"></div>
<div class="abs news" style="top:3470px"><span class="news-thumb"></span><div><p class="news-title">Planning your first social media campaign with ease</p><p class="news-date">Feb 21, 2017</p></div></div>

<p class="abs foot-head" style="top:3298px;left:795px">SUBSCRIBE</p>
<p class="abs subscribe-text" style="top:3330px">Get our monthly tips on design, search and social marketing straight to your inbox.</p>
<div class="abs sub-field"><span>Your email</span><b><svg width="12" height="12" viewBox="0 0 12 12"><path d="M1 6h9M6 2l4 4-4 4" fill="none" stroke="#fff" stroke-width="1.5"/></svg></b></div>
<p class="abs sub-note">*We never share your email.</p>

<div class="abs bottom-bar"></div>
<p class="abs copyright">© 2017. All rights reserved</p>
<span class="abs social" style="left:874px"></span>
<span class="abs social" style="left:910px"></span>
<span class="abs social" style="left:944px"></span>

</body>
</html>
```